Article/Flyer - Reservation of Rights

We would like an article that we normally produce through illustrator in a pdf format to be placed in a Word format. We have provided a sample article/flyer of our normal distribution style. We would like the outcome to be in WORD format

```html
<!DOCTYPE html>
<html lang="en">
<head>
<meta charset="utf-8">
<title>Reservation of Rights Letter – Kestrel Risk Advisors</title>
<link href="https://fonts.googleapis.com/css2?family=Arimo:wght@400;700&display=swap" rel="stylesheet">
<style>
  :root {
    --brand-red: #c3262c;
    --ink-dark: #2a2a2a;
    --sky-light: #b9d8ea;
    --sky-mid: #6fb0d6;
    --sky-deep: #2f82b8;
    --text-light: #ffffff;
    --header-white: #ffffff;
  }
  * { margin: 0; padding: 0; box-sizing: border-box; }
  html, body { width: 927px; height: 1200px; overflow: hidden; background: #ffffff; }
  .flyer {
    position: relative; width: 927px; height: 1200px; overflow: hidden;
    font-family: "Arimo", Arial, sans-serif; color: var(--text-light);
  }
  .cityscape {
    position: absolute; inset: 0;
    background:
      radial-gradient(ellipse at 20% 15%, rgba(255,255,255,0.55), rgba(255,255,255,0) 45%),
      linear-gradient(160deg, var(--sky-light) 0%, var(--sky-mid) 40%, var(--sky-deep) 100%);
  }
  .masthead {
    position: absolute; left: 0; top: 0; width: 600px; height: 150px;
    background: linear-gradient(90deg, var(--header-white) 70%, rgba(255,255,255,0));
  }
  .brand-name {
    position: absolute; left: 82px; top: 34px;
    font-family: "Arimo", Arial, sans-serif; font-weight: 700;
    font-size: 36px; color: var(--ink-dark); line-height: 1;
  }
  .brand-tagline {
    position: absolute; left: 83px; top: 82px;
    font-size: 14px; color: var(--ink-dark); white-space: nowrap;
  }
  .brand-legal {
    position: absolute; left: 83px; top: 106px;
    font-size: 12px; color: var(--ink-dark); white-space: nowrap;
  }
  .team-photo {
    position: absolute; right: 0; top: 0; width: 370px; height: 185px;
    background: linear-gradient(120deg, #dfe6ea 0%, #b9c6cf 40%, #8c9ba6 70%, #cfd8de 100%);
  }
  .intro-band {
    position: absolute; left: 0; top: 177px; width: 927px; height: 96px;
    background: linear-gradient(90deg, var(--brand-red) 0%, var(--brand-red) 70%, rgba(195,38,44,0.85) 100%);
    padding: 10px 84px 0 121px;
    font-weight: 700; font-size: 16px; line-height: 22.5px;
  }
  .section { position: absolute; left: 0; width: 927px; }
  .section-tab {
    height: 26px; width: 460px; margin-left: 60px;
    background: linear-gradient(90deg, var(--brand-red) 0%, var(--brand-red) 80%, rgba(195,38,44,0) 100%);
    font-weight: 700; font-size: 18.5px; line-height: 26px; padding-left: 8px;
  }
  .section-body { padding: 3px 32px 0 68px; }
  .section-body p { font-size: 16.3px; line-height: 19.5px; margin-bottom: 8px; }
  .section-body p.tight { margin-bottom: 0; }
  .s1 { top: 291px; }
  .s2 { top: 571px; }
  .s3 { top: 959px; }
</style>
</head>
<body>
<main class="flyer">
  <div class="cityscape" role="img" aria-label="Blue-tinted cityscape of glass office towers"></div>

  <header class="masthead">
    <div class="brand-name">Kestrel Risk Advisors</div>
    <div class="brand-tagline">Insurance for Design and Environmental Professionals</div>
    <div class="brand-legal">Summit Risk Partners of Oregon, LLC dba Kestrel Risk Advisors</div>
  </header>
  <div class="team-photo" role="img" aria-label="Photograph of three professionals reviewing plans in an office"></div>

  <div class="intro-band">Reporting a claim or potential claim to your professional liability insurance company will trigger a fair amount of return correspondence that often creates confusion rather than clarity. One document that commonly falls into this category is the Reservation of Rights Letter.</div>

  <section class="section s1">
    <h2 class="section-tab">What is the Reservation of Rights Letter</h2>
    <div class="section-body">
      <p>The Reservation of Rights Letter is a normal part of the insurance claims process. Its purpose is to provide notification from the insurance company to the policy holder that coverage may not apply. While this often comes as alarming news, the Reservation of Rights Letter should not be mistaken as an outright denial -- it does not automatically mean that coverage is being or will be denied.</p>
      <p>This standard correspondence is routinely sent to comply with state laws and preserve the insurance company’s legal ability to deny some, or all, of the claim pending further investigation while the claim is ongoing and being handled by the insurance company. Failure to send the letter could be considered a waiver of their rights at a later time.</p>
      <p>Because information is vague in the early stages of a claim and often is limited to unsubstantiated allegations and a few facts, the Reservation of Rights Letter protects the insurance company’s interests to later deny coverage in whole or part based on evidence revealed during claims handling.</p>
    </div>
  </section>

  <section class="section s2">
    <h2 class="section-tab">Interpreting the Letter</h2>
    <div class="section-body">
      <p>Most of the time the Reservation of Rights Letter is a generic form letter that states your insurance company is proceeding with handling your claim but reserves the right to deny coverage later on based upon any information that reveals reason to deny.</p>
      <p>Legitimate reasons an insurance company may deny coverage include when the loss occurred in relation to your retroactive date, specific exclusions in the policy language, prior knowledge of the incident, and coverage by another policy, among others.</p>
      <p>If the insurance company believes there may be reason for denial at the time the Reservation of Rights Letter is sent, it will be stated in the letter. For example, if the claim alleges breach of warranty, the letter will state that warranties are specifically excluded by the policy and it will include the policy language to demonstrate the exclusion.</p>
      <p class="tight">Even when specific reasons for potential coverage denial are cited, it is important to note that this is not a final verdict nor does it mean complete lack of coverage. Generally the insurance company is obligated to help you if any of your claims are covered by your insurance policy – there is a duty to defend. In cases such as the scenario above, circumstances of the claim will influence what is covered and what may be subject to exclusion.</p>
      <p>Based on investigative conclusions, the insurance company may not be obligated to pay the damages for certain types or aspects of claims.</p>
    </div>
  </section>

  <section class="section s3">
    <h2 class="section-tab">How to Proceed</h2>
    <div class="section-body">
      <p>Although the intent of the Reservation of Rights Letter is to protect the insurance company’s interests, it also alerts the policy holder to the fact that some elements of a claim may not be covered and therefore allows the insured to take steps to protect its potentially uninsured interests.</p>
      <p>However, receiving the Reservation of Rights Letter and even the insurance company’s interpretation of the policy language or law that they believe points toward coverage declination does not mean that you are automatically required to accept a denial of coverage.</p>
      <p>The best thing to do upon receiving the letter is to contact your broker and work closely with them and the insurance company claims handling department to ensure the prompt and fair handling of your claim.</p>
    </div>
  </section>
</main>
</body>
</html>
```